Business card design for upmarket Home Technology design and Installation company

Hello designers, we need a great business card designed.
We need it to convey high tech, and also sophistication .
We work with some of the most affluent people in the world building them home technology systems, and A/V entertainment systems.

Services offered include the following:
Design, sales, installation, and maintenance of

*Home Automation systems
*Distributed / Multi-Room Audio and Video
*High Performance Networks & WiFi
* Lighting and Shade Control
*Home cinema
*Security and CCTV Systems

I have included a copy of our logo to use for your design efforts.

Target Market(s)

Upmarket clients with multi million euro villas.

Industry/Entity Type

Home technology

Contact Information for Business Card

NAME: Derek Halvin ADDRESS: Carrer Bellamar Local 42, Cala Torrent, 07293 PHONE: +34-652-918-204 EMAIL: DHalvin@VORTELhomesystems.example WEB: www.vortelhomesystems.example

Requirements
Must have
• Our Logo, and our tagline

```html
<!DOCTYPE html>
<html lang="en">
<head>
<meta charset="utf-8">
<title>VORTEL – Business Card</title>
<link href="https://fonts.googleapis.com/css2?family=Lato:wght@300;400;700;900&display=swap" rel="stylesheet">
<style>
  :root{
    --bg:#4a4a49;
    --card:#ffffff;
    --gold:#b8903f;
    --gold-light:#d9b66a;
    --ink:#222222;
    --on-gold:#ffffff;
  }
  *{box-sizing:border-box;margin:0;padding:0}
  html,body{width:1200px;height:801px;overflow:hidden}
  body{background:var(--bg);font-family:'Lato',sans-serif;position:relative}
  .card{position:absolute;top:246px;width:540px;height:309px;background:var(--card);border-radius:16px;overflow:hidden}
  .card--front{left:40px;border:2px solid var(--gold)}
  .card--back{left:620px}

  /* front */
  .wordmark-large{position:absolute;left:34px;right:34px;top:40px;display:flex;align-items:center;gap:16px;color:var(--gold);font-weight:300;font-size:86px;letter-spacing:10px;line-height:1;white-space:nowrap}
  .wordmark-large .dot{width:22px;height:22px;border-radius:50%;background:var(--gold);flex:none}
  .band-main{position:absolute;left:0;right:0;top:168px;height:70px;background:var(--gold);color:var(--on-gold)}
  .person{position:absolute;left:26px;top:14px}
  .person-name{font-weight:900;font-size:22px;line-height:1.1}
  .person-role{font-weight:400;font-size:13px;margin-top:3px;letter-spacing:.5px}
  .band-ring{position:absolute;left:206px;top:-8px;width:86px;height:86px;border-radius:50%;background:var(--card);display:flex;align-items:center;justify-content:center}
  .band-ring span{width:58px;height:58px;border-radius:50%;border:9px solid var(--gold)}
  .contact{position:absolute;left:308px;top:10px;list-style:none;font-size:10.5px;line-height:17px}
  .contact li{display:flex;align-items:center;gap:6px;white-space:nowrap}
  .contact svg{width:10px;height:10px;flex:none;fill:var(--on-gold)}
  .band-address{position:absolute;left:0;right:0;top:244px;height:30px;background:var(--gold);color:var(--on-gold);font-size:13px;letter-spacing:.6px;display:flex;align-items:center;justify-content:center}

  /* back */
  .brand{position:absolute;left:0;right:0;top:44px;display:flex;flex-direction:column;align-items:center;gap:12px}
  .brand-circle{width:72px;height:72px;border-radius:50%;border:11px solid var(--gold)}
  .brand-name{color:var(--gold);font-weight:300;font-size:34px;letter-spacing:9px;line-height:1}
  .divider{position:absolute;left:28px;right:28px;top:182px;height:1.5px;background:var(--gold)}
  .services-pill{position:absolute;left:50%;top:169px;transform:translateX(-50%);background:var(--gold);color:var(--on-gold);font-weight:700;font-size:13px;letter-spacing:1px;padding:6px 22px;border-radius:14px}
  .services{position:absolute;top:210px;list-style:none;font-size:12.5px;line-height:20px;color:var(--ink)}
  .services--left{left:34px}
  .services--right{left:326px}
  .services li{display:flex;align-items:center;gap:8px}
  .services li::before{content:"";width:6px;height:6px;border-radius:50%;background:var(--gold);flex:none}
</style>
</head>
<body>
  <section class="card card--front" aria-label="Business card front">
    <div class="wordmark-large"><span>VORTEL</span><span class="dot"></span></div>
    <div class="band-main">
      <div class="person">
        <p class="person-name">Derek Halvin</p>
        <p class="person-role">Managing Director</p>
      </div>
      <div class="band-ring"><span></span></div>
      <ul class="contact">
        <li><svg viewBox="0 0 10 10"><path d="M2 0.5l2 2-1 1.2a6 6 0 0 0 3.3 3.3l1.2-1 2 2-1.3 1.5C4.5 9.5.5 5.5.5 1.8z"/></svg>+34-652-918-204</li>
        <li><svg viewBox="0 0 10 10"><path d="M0 2h10v6H0zM0 2l5 3.5L10 2v1L5 6.5 0 3z" fill-rule="evenodd"/></svg>DHalvin@VORTELhomesystems.example</li>
        <li><svg viewBox="0 0 10 10"><circle cx="5" cy="5" r="4.5"/></svg>www.vortelhomesystems.example</li>
      </ul>
    </div>
    <div class="band-address">Carrer Bellamar Local 42, Cala Torrent, 07293</div>
  </section>

  <section class="card card--back" aria-label="Business card back">
    <div class="brand">
      <span class="brand-circle"></span>
      <span class="brand-name">VORTEL</span>
    </div>
    <div class="divider"></div>
    <div class="services-pill">SERVICES</div>
    <ul class="services services--left">
      <li>Home Automation systems</li>
      <li>Distributed / Multi-Room Audio and Video</li>
      <li>High Performance Networks &amp; WiFi</li>
    </ul>
    <ul class="services services--right">
      <li>Lighting and Shade Control</li>
      <li>Home cinema</li>
      <li>Security and CCTV Systems</li>
    </ul>
  </section>
</body>
</html>
```